Brightwave Systems Business Cards
CHANGES::::::::
Dr. Helen T. Caldwell:
1) Cel Phone:
2) Title:
EMR Clinical Content Developer
2nd front of the card:
1) Name:
Dr. Gavin L. Thornby
EMR Implementation Specialist
3) Cel Phone:
4) Email:
gavin.thornby@brightwavesys-pr.example
I'm out...hope you find what you're looking for :)
PLEASE NOTE:
Addres:
Linden Court Plaza #3, Suite 518
San Juan, PR 00947
New phone #:
Fax #:

```html
<!DOCTYPE html>
<html lang="en">
<head>
<meta charset="utf-8">
<title>Brightwave Systems Stationery</title>
<link href="https://fonts.googleapis.com/css2?family=Open+Sans:wght@400;600;700&display=swap" rel="stylesheet">
<style>
:root{
  --stage:#ebe8e4;
  --paper:#ffffff;
  --ink:#3b3b3b;
  --dark:#353535;
  --dark-2:#2a2a2a;
  --orange:#f59a1f;
  --orange-deep:#e2691a;
  --muted:#8a8a8a;
}
*{margin:0;padding:0;box-sizing:border-box}
html,body{width:1200px;height:897px;overflow:hidden}
body{background:var(--stage);font-family:"Open Sans",Arial,sans-serif;color:var(--ink);position:relative}
.brand{display:flex;align-items:center;gap:7px;font-weight:700;color:#fff;white-space:nowrap}
.brand-dot{border-radius:50%;background:var(--orange);flex:none}

/* letterhead */
.letterhead{position:absolute;left:90px;top:41px;width:480px;height:618px;background:var(--paper);box-shadow:0 3px 10px rgba(0,0,0,.25);overflow:hidden}
.letterhead-band{height:52px;background:var(--dark);border-bottom:4px solid var(--orange);display:flex;align-items:center;justify-content:space-between;padding:0 18px}
.letterhead-band .brand{font-size:17px}
.letterhead-band .brand-dot{width:18px;height:18px}
.letterhead-body{position:relative;padding:36px 34px 0 34px;font-size:6.4px;line-height:10px;color:#6b6b6b}
.letterhead-body p{margin-bottom:10px}
.recipient{margin-bottom:20px!important}
.watermark{position:absolute;left:250px;top:360px;width:190px;height:190px;border-radius:50%;background:var(--orange);opacity:.12}
.letterhead-footer{position:absolute;left:0;right:0;bottom:12px;text-align:center;font-size:5.6px;color:var(--muted)}

/* business cards */
.card{position:absolute;width:247px;height:110px;border-radius:10px;overflow:hidden;box-shadow:0 3px 8px rgba(0,0,0,.3)}
.card-front{background:linear-gradient(160deg,#444 0%,var(--dark-2) 100%);color:#fff;padding:9px 12px}
.card-front .brand{font-size:11px}
.card-front .brand-dot{width:11px;height:11px}
.card-front .deco{position:absolute;right:-28px;top:12px;width:110px;height:110px;border-radius:50%;background:var(--orange);opacity:.9}
.card-name{position:relative;margin-top:7px;font-size:8px;font-weight:700;color:var(--orange)}
.card-title{position:relative;font-size:5.4px;color:#ddd;margin-bottom:5px}
.card-contact{position:relative;font-size:5px;line-height:7px;color:#ddd}
.card-back{background:linear-gradient(135deg,var(--orange) 0%,var(--orange-deep) 100%)}
.card-back .deco{position:absolute;left:90px;top:14px;width:66px;height:66px;border-radius:50%;background:#fff;opacity:.85}
.card-web{position:absolute;left:0;right:0;bottom:8px;text-align:center;font-size:5.4px;color:#fff}

/* envelopes */
.envelope{position:absolute;background:var(--paper);box-shadow:0 3px 8px rgba(0,0,0,.25);overflow:hidden}
.envelope-front{left:674px;top:523px;width:327px;height:131px}
.envelope-band{height:40px;background:var(--dark);border-bottom:3px solid var(--orange);display:flex;align-items:center;justify-content:space-between;padding:0 12px}
.envelope-band .brand{font-size:13px}
.envelope-band .brand-dot{width:14px;height:14px}
.return-address{position:absolute;left:16px;top:50px;font-size:5.2px;line-height:7.4px;color:#555}
.address-window{position:absolute;left:20px;top:84px;width:95px;height:32px;border-radius:5px;background:linear-gradient(#8d8d8d,#6c6c6c);border:2px solid #bdbdbd}
.envelope-back{top:693px;height:167px}
.envelope-back svg{position:absolute;inset:0}
.back-left{left:213px;width:357px}
.back-right{left:674px;width:327px}
</style>
</head>
<body>

<section class="letterhead">
  <header class="letterhead-band">
    <div class="brand"><span class="brand-dot"></span>Brightwave Systems</div>
  </header>
  <div class="watermark" role="img" aria-label="Faint brand circle"></div>
  <div class="letterhead-body">
    <p class="recipient">Recipient Name<br>120 Harbor Street<br>San Juan, Puerto Rico</p>
    <p>Dear Recipient Name,</p>
    <p>Thank you for your interest in our clinical software services. This letter outlines the next steps for your team, including scheduling, training sessions and data review. We look forward to supporting your practice through every phase of the project and beyond.</p>
    <p>Our specialists will visit your offices to review current workflows and records. Each visit is planned around your schedule so daily care continues without interruption. A short report with recommendations will follow within two weeks of the final session.</p>
    <p>Please share any questions with your project contact at any time. We value clear communication and will keep you informed of progress at each milestone.</p>
    <p>Thank you again for choosing our team.</p>
    <p style="margin-top:18px">Yours truly,<br>Project Manager</p>
  </div>
  <footer class="letterhead-footer">Linden Court Plaza #3, Suite 518 San Juan, PR 00947 · T 787.555.0142 · F 787.555.0143 · brightwavesys-pr.example</footer>
</section>

<article class="card card-front" style="left:613px;top:97px">
  <div class="deco" role="img" aria-label="Brand circle decoration"></div>
  <div class="brand" style="position:relative"><span class="brand-dot"></span>Brightwave Systems</div>
  <div class="card-name">Dr. Helen T. Caldwell</div>
  <div class="card-title">EMR Clinical Content Developer</div>
  <div class="card-contact">Linden Court Plaza #3, Suite 518<br>San Juan, PR 00947<br>Tel 787.555.0142<br>Cel 787.555.0161<br>helen.caldwell@brightwavesys-pr.example</div>
</article>

<article class="card card-front" style="left:880px;top:97px">
  <div class="deco" role="img" aria-label="Brand circle decoration"></div>
  <div class="brand" style="position:relative"><span class="brand-dot"></span>Brightwave Systems</div>
  <div class="card-name">Dr. Gavin L. Thornby</div>
  <div class="card-title">EMR Implementation Specialist</div>
  <div class="card-contact">Linden Court Plaza #3, Suite 518<br>San Juan, PR 00947<br>Tel 787.555.0142<br>Cel 787.555.0178<br>gavin.thornby@brightwavesys-pr.example</div>
</article>

<article class="card card-back" style="left:613px;top:259px">
  <div class="deco" role="img" aria-label="Brand circle decoration"></div>
  <div class="card-web">www.brightwavesys-pr.example</div>
</article>

<article class="card card-back" style="left:880px;top:259px">
  <div class="deco" role="img" aria-label="Brand circle decoration"></div>
  <div class="card-web">www.brightwavesys-pr.example</div>
</article>

<section class="envelope envelope-front">
  <header class="envelope-band">
    <div class="brand"><span class="brand-dot"></span>Brightwave Systems</div>
  </header>
  <div class="return-address">Linden Court Plaza #3<br>Suite 518, San Juan, PR 00947</div>
  <div class="address-window"></div>
</section>

<section class="envelope envelope-back back-left">
  <svg width="357" height="167" viewBox="0 0 357 167">
    <polygon points="0,0 357,0 178.5,90" fill="#3a3a3a"/>
    <polyline points="0,0 178.5,90 357,0" fill="none" stroke="#d6d6d6" stroke-width="1"/>
    <circle cx="178.5" cy="76" r="11" fill="#f59a1f"/>
  </svg>
</section>

<section class="envelope envelope-back back-right">
  <svg width="327" height="167" viewBox="0 0 327 167">
    <defs>
      <linearGradient id="flapOrange" x1="0" y1="0" x2="0" y2="1">
        <stop offset="0" stop-color="#f59a1f"/>
        <stop offset="1" stop-color="#e2691a"/>
      </linearGradient>
    </defs>
    <polygon points="0,0 327,0 163.5,90" fill="url(#flapOrange)"/>
    <circle cx="163.5" cy="76" r="11" fill="#ffffff"/>
  </svg>
</section>

</body>
</html>
```